Australian small vineyard seeking wine label.

We need a wine label design for a new wine brand \Boutique winery - 2 vintages so far, looking for something a little eye catching, but simple.
Wine label name: Brent and Co
2013 Cabernet Shiraz
2014 Shiraz
Estate grown
Vineyard located at Sevenhill in the Clare valley South Australia.

Target Market(s)

ladies aged between 20 and 50

Industry/Entity Type

Boutique

Logo Text

Brent and Co

Logo styles of interest
Emblem Logo
Pictorial/Combination Logo
Abstract Logo
Character Logo
Font styles to use
Serif
Script

Requirements
Must have
• easy to read text
Nice to have
• The grape grower and winemaker is Martin Brent -
• had some thoughts of Captain Brent - Australian - naval flag
• But very open to ideas
Should not have
• over complications and colors due to cost of wine label being determined by amount of colors required abd print set up.

```html
<!DOCTYPE html>
<html lang="en">
<head>
<meta charset="utf-8">
<title>Brent and Co — Vintage 2013 Cabernet Shiraz Label</title>
<link href="https://fonts.googleapis.com/css2?family=Cormorant+SC:wght@500;600&family=Cormorant+Garamond:ital,wght@0,600;1,700&display=swap" rel="stylesheet">
<style>
  :root {
    --backdrop: #dfe5ec;
    --paper: #f3f1ee;
    --wine: #6b2a2b;
    --wine-text: #6e3a3a;
    --band-text: #f3ece6;
    --vine-light: #c7b3ad;
    --vine-dark: #8a6560;
  }
  * { margin: 0; padding: 0; box-sizing: border-box; }
  html, body {
    width: 740px;
    height: 1200px;
    overflow: hidden;
    background: var(--backdrop);
  }
  .canvas {
    position: relative;
    width: 740px;
    height: 1200px;
  }
  .label {
    position: absolute;
    left: 90px;
    top: 254px;
    width: 560px;
    height: 692px;
    background: var(--paper);
    border-radius: 14px;
    color: var(--wine-text);
    text-align: center;
  }
  .label__frame {
    position: absolute;
    inset: 15px;
    border: 1.5px solid var(--wine);
  }
  .label__country {
    position: absolute;
    top: 44px;
    left: 0;
    right: 0;
    font-family: "Cormorant SC", serif;
    font-weight: 500;
    font-size: 34px;
    line-height: 1.1;
    letter-spacing: 2px;
  }
  .label__brand {
    position: absolute;
    top: 92px;
    left: 0;
    right: 0;
    font-family: "Cormorant Garamond", serif;
    font-weight: 600;
    font-size: 68px;
    line-height: 1;
    color: var(--wine);
  }
  .label__rule {
    position: absolute;
    height: 0;
    border-top: 1.5px solid var(--wine);
  }
  .label__rule--brand { top: 180px; left: 50px; right: 50px; }
  .label__rule--estate-top { top: 418px; left: 165px; right: 150px; border-top-width: 1px; }
  .label__rule--estate-bottom { top: 468px; left: 150px; right: 165px; border-top-width: 1px; }
  .label__vine {
    position: absolute;
    top: 208px;
    left: 152px;
    width: 256px;
    height: 180px;
  }
  .label__estate {
    position: absolute;
    top: 424px;
    left: 0;
    right: 0;
    font-family: "Cormorant SC", serif;
    font-weight: 600;
    font-size: 28px;
    line-height: 1.1;
    letter-spacing: 2px;
  }
  .label__band {
    position: absolute;
    top: 488px;
    left: 15px;
    right: 15px;
    bottom: 15px;
    background: var(--wine);
    color: var(--band-text);
  }
  .label__vintage {
    margin-top: 16px;
    font-family: "Cormorant Garamond", serif;
    font-style: italic;
    font-weight: 700;
    font-size: 42px;
    line-height: 1.1;
    letter-spacing: 1px;
  }
  .label__variety {
    font-family: "Cormorant SC", serif;
    font-weight: 500;
    font-size: 40px;
    line-height: 1.1;
    letter-spacing: 1.5px;
  }
  .label__region {
    margin-top: 8px;
    font-family: "Cormorant SC", serif;
    font-weight: 500;
    font-size: 16px;
    line-height: 1.05;
    letter-spacing: 0.5px;
  }
</style>
</head>
<body>
<main class="canvas">
  <section class="label">
    <div class="label__frame"></div>
    <p class="label__country">Australia</p>
    <h1 class="label__brand">Brent and Co</h1>
    <div class="label__rule label__rule--brand"></div>
    <svg class="label__vine" viewBox="0 0 256 180" role="img" aria-label="Illustration of grape vine leaves with three hanging grape bunches">
      <defs>
        <radialGradient id="vineTone" cx="50%" cy="40%" r="60%">
          <stop offset="0%" stop-color="#8a6560"/>
          <stop offset="100%" stop-color="#c7b3ad"/>
        </radialGradient>
      </defs>
      <rect width="256" height="180" rx="10" fill="url(#vineTone)" opacity="0.7"/>
    </svg>
    <div class="label__rule label__rule--estate-top"></div>
    <p class="label__estate">Estate Grown</p>
    <div class="label__rule label__rule--estate-bottom"></div>
    <div class="label__band">
      <p class="label__vintage">VINTAGE 2013</p>
      <p class="label__variety">Cabernet Shiraz</p>
      <p class="label__region">Sevenhill - Clare Valley<br>South Australia</p>
    </div>
  </section>
</main>
</body>
</html>
```